Corvane Project Services - Flyer

Project Breif:
I need a single page A4 Capability Statement, which will be used to market our services to prospective clients, both in print and via email PDF.
It needs to look professional and should incorporate the elements I have uploaded into files, these include:
Capability Statement Text
Corvane Services Company Logo
Additional Logo’s (Tools We Use)
Glimmer Bay Pics can be cut into the page
I have included examples of capability statements as a guide to what i am looking for.
Regards
Derek
Engineering Consulting

```html
<!DOCTYPE html>
<html lang="en">
<head>
<meta charset="utf-8">
<title>Corvane Project Services – Capability Statement</title>
<link rel="stylesheet" href="https://fonts.googleapis.com/css2?family=Outfit:wght@300;400;600;700&family=Arimo:wght@400;700&display=swap">
<style>
  :root {
    --brand-blue: #0a4fc0;
    --accent-cyan: #1ea0c8;
    --ink: #111111;
    --body-ink: #2b2b2b;
    --rule: #9a9a9a;
    --page-bg: #ffffff;
    --sheet-bg: #ffffff;
  }
  * { box-sizing: border-box; margin: 0; padding: 0; }
  html, body { width: 1200px; height: 832px; overflow: hidden; background: var(--page-bg); }
  .flyer {
    position: absolute; left: 310px; top: 63px; width: 512px; height: 724px;
    background: var(--sheet-bg); overflow: hidden;
    font-family: "Arimo", Arial, sans-serif; color: var(--body-ink);
  }
  .flyer__topbar { position: absolute; left: 0; top: 0; width: 100%; height: 8px; background: var(--brand-blue); }
  .masthead { position: absolute; left: 0; top: 8px; width: 100%; height: 100px; }
  .brand { position: absolute; left: 26px; top: 22px; width: 120px; display: flex; flex-direction: column; align-items: center; gap: 6px; }
  .brand__mark { width: 32px; height: 32px; border-radius: 50%; background: var(--brand-blue); }
  .brand__name { font-family: "Outfit", sans-serif; font-weight: 600; font-size: 9.5px; line-height: 1.15; color: var(--ink); text-align: center; letter-spacing: 0.3px; text-transform: uppercase; }
  .masthead__titles { position: absolute; right: 32px; top: 30px; text-align: right; }
  .masthead__title { font-family: "Outfit", sans-serif; font-weight: 700; font-size: 25px; line-height: 1; color: var(--ink); letter-spacing: -0.2px; }
  .masthead__subtitle { font-family: "Outfit", sans-serif; font-weight: 300; font-size: 18.5px; line-height: 1; color: var(--ink); margin-top: 5px; }
  .hero-photo { position: absolute; left: 0; top: 108px; width: 100%; height: 125px;
    background: linear-gradient(100deg, #c9cfda 0%, #eef1f6 35%, #dfe5ef 65%, #c7d0e2 100%); }
  .intro { position: absolute; left: 31px; top: 254px; width: 224px; }
  .intro__headline { font-family: "Outfit", sans-serif; font-weight: 600; font-size: 16px; line-height: 20.5px; color: var(--accent-cyan); }
  .intro__body { margin-top: 16px; }
  .intro__body p { font-size: 8.3px; line-height: 11px; margin-bottom: 11px; }
  .meeting-photo { position: absolute; left: 31px; top: 509px; width: 212px; height: 135px;
    background: linear-gradient(135deg, #e7ebf0 0%, #cfd6df 50%, #dfe4ea 100%); }
  .column-rule { position: absolute; left: 264px; top: 259px; width: 1px; height: 385px; background: var(--rule); }
  .services { position: absolute; left: 283px; top: 254px; width: 210px; }
  .section-title { font-family: "Outfit", sans-serif; font-weight: 600; font-size: 16px; line-height: 20px; color: var(--accent-cyan); margin-bottom: 7px; }
  .service-group { margin-bottom: 11px; }
  .service-group__title { font-size: 8px; font-weight: 700; line-height: 11.2px; color: var(--ink); }
  .service-group ul { list-style: none; }
  .service-group li { font-size: 8px; line-height: 11.2px; }
  .service-group li::before { content: "• "; }
  .contact { position: absolute; left: 283px; top: 552px; width: 210px; }
  .contact p { font-size: 8px; line-height: 11.2px; }
  .contact strong { color: var(--ink); }
  .contact__phone { display: flex; align-items: center; gap: 4px; }
  .contact__phone svg { width: 10px; height: 10px; }
  .flyer__footer { position: absolute; left: 0; top: 663px; width: 100%; height: 61px; background: var(--brand-blue);
    display: flex; align-items: center; justify-content: space-between; padding: 0 32px 0 31px; }
  .footer__url { font-family: "Outfit", sans-serif; font-weight: 600; font-size: 13px; color: #ffffff; }
  .footer__social { display: flex; gap: 4px; }
  .footer__social span { width: 19px; height: 19px; border-radius: 50%; border: 1.5px solid #ffffff; }
</style>
</head>
<body>
  <article class="flyer">
    <div class="flyer__topbar"></div>
    <header class="masthead">
      <div class="brand">
        <div class="brand__mark"></div>
        <div class="brand__name">Corvane Project Services</div>
      </div>
      <div class="masthead__titles">
        <h1 class="masthead__title">Capability Statement</h1>
        <p class="masthead__subtitle">Change Management</p>
      </div>
    </header>
    <div class="hero-photo" role="img" aria-label="Photo of a pen resting on a printed project Gantt chart"></div>

    <section class="intro">
      <h2 class="intro__headline">Corvane Project Services Ltd. Is A Leading Project Control Consultancy Based In Co Cork Ireland</h2>
      <div class="intro__body">
        <p>For over 20 years we have been helping our clients to deliver complex projects and programs throughout mainland Europe.</p>
        <p>We are passionate about empower organisations to achieve their objectives, on time and on budget.</p>
        <p>We are continually innovating, evolving and learning, utilize the latest industry tools and techniques to deliver real value to our clients.</p>
        <p>Our goal is to make successful project delivery more achievable and repeatable.</p>
      </div>
    </section>
    <div class="meeting-photo" role="img" aria-label="Photo of hands reviewing documents at a meeting table"></div>

    <div class="column-rule"></div>

    <section class="services">
      <h2 class="section-title">Core Services</h2>
      <div class="service-group">
        <h3 class="service-group__title">Planning and Scheduling</h3>
        <ul>
          <li>Tender Planning</li>
          <li>Interactive Planning / Pull Planning</li>
          <li>EPCMV Planning &amp; Scheduling</li>
          <li>Schedule Earned Value Management</li>
          <li>Independent Schedule Quality Assessment</li>
          <li>Schedule Risk Analysis (Monte Carlo)</li>
          <li>Training</li>
        </ul>
      </div>
      <div class="service-group">
        <h3 class="service-group__title">Management of Risk</h3>
        <ul>
          <li>Risk Management Policies &amp; Procedures</li>
          <li>Risk Management Strategy</li>
          <li>Risk Registers</li>
          <li>Risk Improvement Planning</li>
          <li>Risk Response and Communication</li>
          <li>Risk Management Training</li>
        </ul>
      </div>
      <div class="service-group">
        <h3 class="service-group__title">Cost Control:</h3>
        <ul>
          <li>Estimating &amp; Forecasting</li>
          <li>Earned Value Analysis</li>
          <li>Progress Reporting</li>
          <li>Cost Risk Analysis</li>
        </ul>
      </div>
    </section>

    <section class="contact">
      <h2 class="section-title">Contact Us:</h2>
      <p><strong>Derek Halloran</strong> (Managing Director)</p>
      <p>info@corvaneservices.ie</p>
      <p>www.corvaneservices.ie</p>
      <p class="contact__phone">
        <svg viewBox="0 0 10 10" aria-hidden="true"><rect width="10" height="10" fill="var(--accent-cyan)"/><path d="M2.6 2.2l1.3-.2.6 1.6-.8.6a4 4 0 0 0 2.1 2.1l.6-.8 1.6.6-.2 1.3C5.3 7.6 2.4 4.7 2.6 2.2z" fill="#fff"/></svg>
        +353 (0)875550142
      </p>
    </section>

    <footer class="flyer__footer">
      <span class="footer__url">www.corvaneservices.ie</span>
      <div class="footer__social" aria-hidden="true"><span></span><span></span><span></span></div>
    </footer>
  </article>
</body>
</html>
```